30th birthday flyer

I would like a flyer made up for my 30th birthday.
The event will be held on boat, and cruise the river
Theme on flyer nautical, Boat party,
Vessel is : MV MARENDO
Flyer must include:

Friday 06th April 5:00PM to 8:30PM
58 Wattlebrook Parade, Noosaville, QLD
Food and Booze provided

```html
<!DOCTYPE html>
<html lang="en">
<head>
<meta charset="utf-8">
<title>30th Birthday Boat Party Flyer</title>
<link href="https://fonts.googleapis.com/css2?family=Cinzel:wght@400;500;700&display=swap" rel="stylesheet">
<style>
  :root {
    --mat: #6d6e71;
    --ink: #050505;
    --panel: #0a0a0a;
    --gold: #e8c77a;
    --gold-line: #c8923a;
    --silver: #f4f4f4;
    --white: #ffffff;
  }
  * { margin: 0; padding: 0; box-sizing: border-box; }
  html, body {
    width: 924px; height: 1200px; overflow: hidden;
    background: var(--mat);
  }
  .flyer {
    position: absolute; left: 100px; top: 88px;
    width: 724px; height: 1024px;
    background: var(--ink);
    overflow: hidden;
    font-family: "Cinzel", serif;
    text-align: center;
  }
  .party-backdrop {
    position: absolute; left: 0; top: 0; width: 724px; height: 500px;
    background:
      radial-gradient(circle at 80px 70px, rgba(232,180,90,.55), transparent 110px),
      radial-gradient(circle at 560px 330px, rgba(230,160,40,.6), transparent 120px),
      radial-gradient(circle at 70px 360px, rgba(255,240,210,.35), transparent 70px),
      radial-gradient(circle at 660px 320px, rgba(255,240,210,.35), transparent 70px),
      radial-gradient(circle at 220px 130px, rgba(120,100,70,.35), transparent 90px),
      #0d0d0d;
  }
  .guest-portrait {
    position: absolute; left: 104px; top: 0; width: 464px; height: 500px;
    background: linear-gradient(180deg, #2a2420 0%, #8a6a5a 22%, #ead8c8 42%, #e7a6b0 70%, #e4c8c0 100%);
    border-radius: 160px 160px 0 0;
  }
  .curves { position: absolute; left: 0; top: 0; }
  .headline-age {
    position: absolute; left: 0; right: 0; top: 538px;
    font-size: 50px; font-weight: 400; color: var(--gold);
    line-height: 1; font-style: italic; letter-spacing: 1px;
  }
  .headline-main {
    position: absolute; left: 0; right: 0; top: 584px;
    font-size: 112px; font-weight: 700; line-height: 1;
    letter-spacing: 2px;
    color: var(--silver);
    background: linear-gradient(180deg, #ffffff 0%, #e6e6e6 55%, #9a9a9a 100%);
    -webkit-background-clip: text; background-clip: text;
    -webkit-text-fill-color: transparent;
    filter: drop-shadow(2px 3px 0 #3a3a3a);
  }
  .event-date, .event-time {
    position: absolute; left: 0; right: 0;
    font-size: 33px; font-weight: 500; color: var(--gold); line-height: 1;
  }
  .event-date { top: 752px; }
  .event-time { top: 790px; }
  .event-date .ordinal { font-size: 26px; }
  .wave-divider { position: absolute; left: 162px; top: 838px; }
  .venue-note {
    position: absolute; left: 0; right: 0; top: 864px;
    font-size: 30px; color: var(--white); line-height: 34px; font-weight: 400;
    letter-spacing: -0.5px;
  }
  .vessel-name {
    position: absolute; left: 0; right: 0; top: 944px;
    font-size: 16px; color: var(--gold); letter-spacing: .5px;
  }
  .venue-address {
    position: absolute; left: 0; right: 0; top: 970px;
    font-size: 14px; color: var(--white); letter-spacing: .5px;
  }
  .catering-note {
    position: absolute; left: 0; right: 0; top: 992px;
    font-size: 14px; color: var(--gold); letter-spacing: .5px;
  }
</style>
</head>
<body>
<main class="flyer">
  <div class="party-backdrop" role="img" aria-label="Dark party backdrop with golden fireworks, streamers and champagne bottles splashing"></div>
  <div class="guest-portrait" role="img" aria-label="Photo of the birthday guest in a captain's hat and pink floral shirt"></div>

  <svg class="curves" width="724" height="1024" viewBox="0 0 724 1024" aria-hidden="true">
    <defs>
      <radialGradient id="glow">
        <stop offset="0" stop-color="#fff3d0" stop-opacity=".9"/>
        <stop offset="1" stop-color="#e8a040" stop-opacity="0"/>
      </radialGradient>
    </defs>
    <path d="M0 420 Q362 560 724 428 L724 1024 L0 1024 Z" fill="#0a0a0a"/>
    <path d="M0 420 Q362 560 724 428" fill="none" stroke="#c8923a" stroke-width="2"/>
    <path d="M0 756 Q362 650 724 794" fill="none" stroke="#c8923a" stroke-width="2"/>
    <circle cx="20" cy="780" r="30" fill="url(#glow)"/>
    <circle cx="362" cy="476" r="22" fill="url(#glow)"/>
  </svg>

  <p class="headline-age">30TH</p>
  <h1 class="headline-main">BIRTHDAY</h1>
  <p class="event-date">FRIDAY 06<span class="ordinal">TH</span> APRIL</p>
  <p class="event-time">5:00PM TO 8:30PM</p>
  <svg class="wave-divider" width="400" height="14" viewBox="0 0 400 14" aria-hidden="true">
    <path d="M0 7 Q25 0 50 7 T100 7 T150 7 T200 7 T250 7 T300 7 T350 7 T400 7" fill="none" stroke="#c8923a" stroke-width="1.5"/>
  </svg>
  <p class="venue-note">EVENT WILL BE HELD ON BOAT,<br>AND CRUISE THE RIVER</p>
  <p class="vessel-name">VESSEL IS : MV MARENDO</p>
  <p class="venue-address">58 WATTLEBROOK PARADE, NOOSAVILLE, QLD</p>
  <p class="catering-note">FOOD AND BOOZE PROVIDED</p>
</main>
</body>
</html>
```